Meridian Rest Supply Needs Business Card

Looking for a very nice looking business card. Creative but not extravagant. We sell beds and pillows across the U.S. and need something professional but catchy. I have attached the logo.

Name : Dale Fenwick
Title : President
Phone : (800) 417-2964
Email: sleep@quorvana.com
Website: www.quorvana.com

Can be single-sided or double-sided
horizontal or vertical

Can use Blues/Greys

Target Market(s)

Mass Market

Industry/Entity Type

Retail

Contact Information for Business Card

Name : Dale Fenwick
Title : President
Phone : (800) 417-2964
Email: sleep@quorvana.com
Website: www.quorvana.com

Requirements
Must have
• Clean, Modern, Smooth
• Can use Blues/Greys
• On the other side without the information - have something simple like www.quorvana.com or our logo
Nice to have
• Surprise me
Should not have
• Nothing crazy, nothing cluttered

```html
<!DOCTYPE html>
<html lang="en">
<head>
<meta charset="utf-8">
<title>Quorvana Business Card</title>
<link href="https://fonts.googleapis.com/css2?family=Source+Sans+3:wght@400;600&display=swap" rel="stylesheet">
<style>
  :root {
    --page: #f1f1f1;
    --card-light: #e3e3e3;
    --brand-blue: #35a5d8;
    --ink: #2a2a2a;
    --white: #ffffff;
    --band-light: #ececec;
  }
  html, body {
    margin: 0;
    width: 1200px;
    height: 900px;
    overflow: hidden;
    background: var(--page);
  }
  .canvas {
    position: relative;
    width: 1200px;
    height: 900px;
  }
  .card {
    position: absolute;
    overflow: hidden;
    box-shadow: 0 4px 14px rgba(0,0,0,0.12);
  }
  .card-front {
    left: 78px; top: 35px;
    width: 587px; height: 363px;
    background: var(--card-light);
  }
  .card-back {
    left: 388px; top: 505px;
    width: 567px; height: 352px;
    background: var(--brand-blue);
  }
  .brand-name {
    position: absolute;
    left: 0; right: 0;
    text-align: center;
    font-family: "Source Sans 3", sans-serif;
    font-weight: 400;
    font-size: 72px;
    line-height: 1;
  }
  .card-front .brand-name {
    top: 89px;
    color: var(--brand-blue);
  }
  .card-back .brand-name {
    top: 147px;
    color: var(--white);
  }
  .contact {
    position: absolute;
    right: 290px;
    top: 266px;
    text-align: right;
    font-family: "Source Sans 3", sans-serif;
    font-size: 16px;
    color: var(--ink);
    line-height: 24px;
  }
  .contact-row {
    display: flex;
    align-items: center;
    justify-content: flex-end;
    gap: 8px;
  }
  .contact-icon { width: 12px; height: 12px; }
  .person {
    position: absolute;
    left: 333px;
    top: 266px;
    font-family: "Source Sans 3", sans-serif;
    line-height: 1;
  }
  .person-name {
    font-size: 22px;
    font-weight: 600;
    color: var(--brand-blue);
  }
  .person-title {
    margin-top: 6px;
    font-size: 17px;
    color: var(--ink);
  }
  .website {
    position: absolute;
    left: 0; right: 0;
    top: 255px;
    text-align: center;
    font-family: "Source Sans 3", sans-serif;
    font-size: 17px;
    letter-spacing: 3.4px;
    color: var(--white);
  }
  .card-band {
    position: absolute;
    left: 0; bottom: 0;
  }
</style>
</head>
<body>
<main class="canvas">

  <section class="card card-front" aria-label="Business card, contact side">
    <div class="brand-name">quorvana</div>

    <div class="contact">
      <div class="contact-row">
        <span>(800) 417-2964</span>
        <svg class="contact-icon" viewBox="0 0 24 24" aria-hidden="true">
          <path fill="var(--brand-blue)" d="M6.6 10.8a15.1 15.1 0 0 0 6.6 6.6l2.2-2.2c.3-.3.7-.4 1-.2 1.1.4 2.300.6 3.6.6.6 0 1 .4 1 1V20c0 .6-.4 1-1 1A17 17 0 0 1 3 4c0-.6.4-1 1-1h3.5c.6 0 1 .4 1 1 0 1.3.2 2.5.6 3.6.1.3 0 .7-.2 1z"/>
        </svg>
      </div>
      <div class="contact-row">
        <span>sleep@quorvana.com</span>
        <svg class="contact-icon" viewBox="0 0 24 24" aria-hidden="true">
          <rect x="2" y="5" width="20" height="14" fill="var(--brand-blue)"/>
          <path d="M2 5l10 8 10-8" fill="none" stroke="var(--card-light)" stroke-width="1.6"/>
        </svg>
      </div>
    </div>

    <div class="person">
      <div class="person-name">Dale Fenwick</div>
      <div class="person-title">President</div>
    </div>

    <svg class="card-band" width="587" height="18" viewBox="0 0 587 18" aria-hidden="true">
      <polygon points="0,0 316,0 302,18 0,18" fill="var(--brand-blue)"/>
      <polygon points="328,0 587,0 587,18 314,18" fill="var(--brand-blue)"/>
    </svg>
  </section>

  <section class="card card-back" aria-label="Business card, brand side">
    <div class="brand-name">quorvana</div>
    <div class="website">www.quorvana.com</div>

    <svg class="card-band" width="567" height="19" viewBox="0 0 567 19" aria-hidden="true">
      <rect x="0" y="0" width="567" height="19" fill="var(--band-light)"/>
      <polygon points="316,0 328,0 314,19 302,19" fill="var(--brand-blue)"/>
    </svg>
  </section>

</main>
</body>
</html>
```